Olmo Restaurant & Bar Menu

Want to make current menu more trendy in design. I have attached a pdf of the menu and of the logo. Rather, than being 6 pages I would like to make the menu into "4 pages". The menu will be printed in color.

I am open to designs that will allow the menu to be printed on 11x17 paper that will be folded in half. The "Breakfast" section needs to be its own page and all the way on the back.

As for the cover I am open to just keeping it as a cover with the info I have on it but completely different design/picture change. The logo needs to stay. The cover can also be used as having menu items on there if pulled of correctly.

The readability has to be clear to the guests.

The restaurant is a Mediterranean style and for the area it is priced mid-high. The atmosphere is casual fine dining with Martini & Wine Bar. All are ingredients are fresh never frozen and everything is prepared from scratch.

Industry/Entity Type

Restaurant

Requirements
Must have
• Breakfast on its own page on the back.
Nice to have
• Trendy Design

```html
<!DOCTYPE html>
<html lang="en">
<head>
<meta charset="utf-8">
<title>Olmo Restaurant &amp; Bar — Menu Spread</title>
<link rel="stylesheet" href="https://fonts.googleapis.com/css2?family=Saira+Condensed:wght@600;700&family=Jost:ital,wght@0,400;0,500;0,600;1,400&display=swap">
<style>
  :root {
    --blue: #29a7df;
    --blue-deep: #1b8fc6;
    --ink: #1d1d1f;
    --muted: #5a5a5e;
    --paper: #ffffff;
    --backdrop: #d6d6d6;
  }
  * { box-sizing: border-box; margin: 0; padding: 0; }
  html, body { width: 1200px; height: 840px; overflow: hidden; }
  body {
    background: var(--backdrop);
    font-family: "Jost", "Futura", sans-serif;
    color: var(--ink);
    position: relative;
  }
  .spread {
    position: absolute; left: 50px; top: 64px;
    width: 1100px; height: 712px;
    display: flex;
    box-shadow: 0 10px 30px rgba(0,0,0,.18);
  }
  .page { position: relative; width: 550px; height: 712px; background: var(--paper); overflow: hidden; }
  .page--back { border-right: 1px solid #e4e4e4; }

  /* ---------- Breakfast page ---------- */
  .breakfast-banner {
    position: absolute; left: 0; top: 26px; width: 298px; height: 34px;
    background: var(--blue); border-radius: 0 17px 17px 0;
    color: #fff; font-family: "Saira Condensed", sans-serif; font-weight: 700;
    font-size: 21px; letter-spacing: .4px; text-transform: uppercase;
    display: flex; align-items: center; padding-left: 24px;
    white-space: nowrap;
  }
  .breakfast-banner small { font-size: 14px; margin-left: 5px; }
  .col { position: absolute; }
  .col--left { left: 30px; top: 74px; width: 236px; }
  .col--right { left: 314px; top: 24px; width: 210px; }
  .section-title {
    font-family: "Saira Condensed", sans-serif; font-weight: 700;
    color: var(--blue); font-size: 21px; line-height: 1; text-transform: uppercase;
    margin: 10px 0 6px;
  }
  .col--right > .section-title:first-child { margin-top: 0; }
  .section-note { font-style: italic; font-size: 9px; color: var(--muted); margin: -2px 0 6px; }
  .item { margin-bottom: 7px; }
  .item__row { display: flex; align-items: baseline; font-size: 11.5px; font-weight: 600; line-height: 1.25; white-space: nowrap; }
  .col--right .item__row { font-size: 11px; }
  .item__row .leader { flex: 1; min-width: 6px; border-bottom: 1px dotted #8a8a8a; margin: 0 4px; transform: translateY(-3px); }
  .item__row .price { font-weight: 500; }
  .item__row--sub { padding-left: 12px; }
  .item__row--sub::before { content: "»"; color: var(--blue); margin-left: -11px; margin-right: 4px; }
  .item__desc { font-size: 8.6px; color: var(--muted); line-height: 1.3; margin-top: 1px; }
  .item--tight { margin-bottom: 3px; }

  .fruit-photo {
    position: absolute; right: 32px; top: 502px; width: 150px; height: 62px;
    border-radius: 4px;
    background: radial-gradient(ellipse at 50% 45%, #f0a24a 0%, #e0503a 45%, #f6ece4 72%, #ffffff 100%);
  }

  .light-breakfast { position: absolute; left: 30px; top: 568px; width: 492px; }
  .light-breakfast .grid { display: grid; grid-template-columns: 1fr 1fr; column-gap: 28px; }

  .back-footer { position: absolute; left: 0; right: 0; bottom: 0; height: 28px; }

  /* ---------- Cover ---------- */
  .cover-topline { position: absolute; left: 0; top: 0; width: 550px; height: 60px; }
  .brand {
    position: absolute; left: 60px; top: 76px;
    display: flex; align-items: center; gap: 12px;
  }
  .brand__mark { width: 44px; height: 44px; background: var(--blue); }
  .brand__name {
    font-family: "Saira Condensed", sans-serif; font-weight: 700;
    font-size: 38px; line-height: 1; color: var(--ink); text-transform: uppercase; letter-spacing: .5px;
  }
  .photo { position: absolute; }
  .photo--steak {
    left: 24px; top: 150px; width: 300px; height: 332px;
    background: radial-gradient(ellipse at 40% 55%, #6b3a22 0%, #4a2818 35%, #9b3b2c 62%, #c9b9ad 100%);
  }
  .photo--seafood {
    left: 332px; top: 150px; width: 194px; height: 160px;
    background: linear-gradient(160deg, #efe9df 0%, #d9c9a8 45%, #c46a3a 70%, #f4f1ec 100%);
  }
  .photo--wraps {
    left: 332px; top: 318px; width: 194px; height: 164px;
    background: linear-gradient(200deg, #e9dcc1 0%, #b48a55 40%, #7a8f3e 62%, #d9c7a7 100%);
  }
  .cover-band { position: absolute; left: 0; top: 470px; width: 550px; height: 242px; }
  .cover-info {
    position: absolute; left: 40px; top: 560px; width: 240px;
    color: #fff; font-family: "Saira Condensed", sans-serif; font-weight: 600;
    text-transform: uppercase; letter-spacing: .6px;
  }
  .cover-info__address { font-size: 14px; white-space: nowrap; }
  .cover-info__phone { font-size: 20px; margin-top: 4px; }
  .cover-info__web { font-size: 17px; margin-top: 22px; }
  .cover-services {
    position: absolute; left: 300px; top: 536px; width: 220px;
    color: #fff; font-family: "Saira Condensed", sans-serif; font-weight: 600;
    font-size: 14px; text-transform: uppercase; letter-spacing: .5px; line-height: 1.25;
    list-style: none;
  }
  .cover-services li { margin-bottom: 14px; }
</style>
</head>
<body>
<main class="spread">

  <!-- Back page: Breakfast -->
  <section class="page page--back" aria-label="Breakfast menu">
    <h1 class="breakfast-banner">Breakfast <small>(Served Saturday &amp; Sunday)</small></h1>

    <div class="col col--left">
      <h2 class="section-title">Skillets</h2>
      <div class="item"><div class="item__row"><span>Veggie</span><span class="leader"></span><span class="price">$6.95</span></div>
        <p class="item__desc">Hash browns, onions, peppers, tomatoes &amp; mushrooms topped with cheese and 2 eggs. Served w/ toast</p></div>
      <div class="item"><div class="item__row"><span>Irish</span><span class="leader"></span><span class="price">$7.95</span></div>
        <p class="item__desc">Hash browns, onions, peppers &amp; corned beef topped with cheese and 2 eggs. Served w/ toast</p></div>
      <div class="item"><div class="item__row"><span>Melting Pot</span><span class="leader"></span><span class="price">$8.95</span></div>
        <p class="item__desc">Hash browns, bacon, sausage, ham, onions &amp; peppers topped with cheese and 2 eggs</p></div>
      <div class="item"><div class="item__row"><span>Biscuits &amp; Gravy</span><span class="leader"></span><span class="price">$7.95</span></div>
        <p class="item__desc">Hash browns, onions &amp; peppers topped w/ homemade biscuits, sausage gravy &amp; 2 eggs</p></div>

      <h2 class="section-title">Omelettes</h2>
      <p class="section-note">Fluffy Three Egg Omelettes, Served w/ Hash Browns &amp; Toast</p>
      <div class="item"><div class="item__row"><span>Athenian</span><span class="leader"></span><span class="price">$8.95</span></div>
        <p class="item__desc">Gyro off-the-cone, tomatoes, onions, olives &amp; feta cheese. Served with cucumber sauce</p></div>
      <div class="item"><div class="item__row"><span>Denver</span><span class="leader"></span><span class="price">$7.95</span></div>
        <p class="item__desc">Ham, onion, pepper &amp; cheese</p></div>
      <div class="item"><div class="item__row"><span>Veggie</span><span class="leader"></span><span class="price">$8.95</span></div>
        <p class="item__desc">Onions, peppers, tomatoes &amp; mushrooms</p></div>
      <div class="item"><div class="item__row"><span>Deluxe</span><span class="leader"></span><span class="price">$8.95</span></div>
        <p class="item__desc">Ham, bacon, sausage, mushrooms, onions, tomatoes and peppers</p></div>
      <div class="item"><div class="item__row"><span>Spinach Pesto</span><span class="leader"></span><span class="price">$8.95</span></div>
        <p class="item__desc">Sundried tomatoes, spinach, mushrooms &amp; cheese. Topped w/ pesto cream sauce</p></div>
      <div class="item"><div class="item__row"><span>Ham &amp; Cheese</span><span class="leader"></span><span class="price">$6.95</span></div></div>
    </div>

    <div class="col col--right">
      <h2 class="section-title">Pancakes, French Toast<br>&amp; Waffles</h2>
      <div class="item item--tight"><div class="item__row"><span>Apple Danish French Toast</span><span class="leader"></span><span class="price">$6.95</span></div></div>
      <div class="item item--tight"><div class="item__row"><span>Bananas Foster Pancakes</span><span class="leader"></span><span class="price">$7.95</span></div></div>
      <div class="item item--tight"><div class="item__row"><span>Strawberry Cake Waffle</span><span class="leader"></span><span class="price">$7.95</span></div></div>
      <div class="item item--tight"><div class="item__row"><span>Pancakes or French Toast</span></div>
        <div class="item__row"><span>2 pcs. $4.55 / 3 pcs.</span><span class="leader"></span><span class="price">$4.95</span></div></div>
      <div class="item item--tight"><div class="item__row"><span>Belgium Waffle</span><span class="leader"></span><span class="price">$4.95</span></div></div>
      <p class="section-note" style="margin-top:2px">Add Fruit Topping, Bacon, Ham or Sausage $1.75</p>

      <h2 class="section-title">Eggs &amp; Specialties</h2>
      <div class="item item--tight"><div class="item__row"><span>Two Eggs, Hash Browns &amp; Toast</span><span class="leader"></span><span class="price">$4.95</span></div></div>
      <div class="item item--tight"><div class="item__row item__row--sub"><span>With Bacon, Sausage or Ham</span><span class="leader"></span><span class="price">$5.95</span></div></div>
      <div class="item item--tight"><div class="item__row item__row--sub"><span>With Corned Beef Hash</span><span class="leader"></span><span class="price">$6.55</span></div></div>
      <div class="item"><div class="item__row item__row--sub"><span>With Gyro off-the-cone</span><span class="leader"></span><span class="price">$6.95</span></div></div>
      <div class="item"><div class="item__row"><span>Steak &amp; Eggs</span><span class="leader"></span><span class="price">$13.95</span></div>
        <p class="item__desc">8oz prime cut steak, 2 eggs, hash browns &amp; toast</p></div>
      <div class="item"><div class="item__row"><span>Chop Steak &amp; Eggs</span><span class="leader"></span><span class="price">$9.95</span></div>
        <p class="item__desc">10oz chopped sirloin steak, 2 eggs, hash browns &amp; toast</p></div>
      <div class="item"><div class="item__row"><span>Granny's Breakfast</span><span class="leader"></span><span class="price">$6.95</span></div>
        <p class="item__desc">Two eggs scrambled w/ potatoes, ham, onions &amp; peppers topped w/ cheese. Served with toast</p></div>
      <div class="item"><div class="item__row"><span>3 Deuces</span><span class="leader"></span><span class="price">$6.95</span></div>
        <p class="item__desc">Two eggs, two pancakes &amp; two sausage links or bacon strips</p></div>
      <div class="item"><div class="item__row"><span>Homemade Biscuits &amp; Gravy</span></div>
        <div class="item__row"><span>Half $3.95 / Full</span><span class="leader"></span><span class="price">$5.95</span></div></div>
    </div>

    <div class="fruit-photo" role="img" aria-label="Photo of a fresh fruit plate with cream"></div>

    <div class="light-breakfast">
      <h2 class="section-title">Light Breakfast</h2>
      <div class="grid">
        <div>
          <div class="item item--tight"><div class="item__row"><span>Egg, Sausage &amp; Cheese Sandwich</span><span class="leader"></span><span class="price">$4.25</span></div></div>
          <div class="item item--tight"><div class="item__row"><span>Oatmeal or Cereal</span><span class="leader"></span><span class="price">$3.55</span></div>
            <div class="item__row"><span>w/ raisins</span><span class="leader"></span><span class="price">$3.95</span></div></div>
          <div class="item item--tight"><div class="item__row"><span>Bagel w/ cream cheese</span><span class="leader"></span><span class="price">$2.55</span></div></div>
        </div>
        <div>
          <div class="item item--tight"><div class="item__row"><span>English Muffin or Raisin Toast</span><span class="leader"></span><span class="price">$1.55</span></div></div>
          <div class="item item--tight"><div class="item__row"><span>Mediterranean Pita</span><span class="leader"></span><span class="price">$6.95</span></div>
            <p class="item__desc">Pesto spread on pita bread w/ spinach, tomatoes, feta &amp; an egg</p></div>
          <div class="item item--tight"><div class="item__row"><span>Fresh Fruit Bowl</span><span class="leader"></span><span class="price">$4.95</span></div></div>
        </div>
      </div>
    </div>

    <svg class="back-footer" viewBox="0 0 550 28" preserveAspectRatio="none" aria-hidden="true">
      <rect x="0" y="2" width="550" height="2" fill="var(--blue)"/>
      <rect x="0" y="10" width="550" height="18" fill="var(--blue)"/>
    </svg>
  </section>

  <!-- Front page: Cover -->
  <section class="page page--cover" aria-label="Menu cover">
    <svg class="cover-topline" viewBox="0 0 550 60" preserveAspectRatio="none" aria-hidden="true">
      <path d="M0 34 Q275 14 550 22 L550 26 Q275 18 0 38 Z" fill="var(--blue)"/>
    </svg>

    <div class="brand">
      <span class="brand__mark" aria-hidden="true"></span>
      <span class="brand__name">Olmo Restaurant &amp; Bar</span>
    </div>

    <div class="photo photo--steak" role="img" aria-label="Photo of a grilled steak with cherry tomatoes and rosemary"></div>
    <div class="photo photo--seafood" role="img" aria-label="Photo of a seafood pasta plate with wine glasses"></div>
    <div class="photo photo--wraps" role="img" aria-label="Photo of gyro pita wraps with sauce"></div>

    <svg class="cover-band" viewBox="0 0 550 242" preserveAspectRatio="none" aria-hidden="true">
      <path d="M0 42 Q275 8 550 30 L550 34 Q275 14 0 48 Z" fill="var(--paper)"/>
      <path d="M0 52 Q275 18 550 40 L550 214 L0 214 Z" fill="var(--blue)"/>
      <rect x="0" y="224" width="550" height="4" fill="var(--blue)"/>
    </svg>

    <div class="cover-info">
      <p class="cover-info__address">48 Harbor Lane · Millbrook, WI 53990</p>
      <p class="cover-info__phone">
        <svg width="14" height="14" viewBox="0 0 24 24" aria-hidden="true" style="vertical-align:-1px"><path fill="#fff" d="M6.6 10.8a15.1 15.1 0 006.6 6.6l2.2-2.2c.3-.3.7-.4 1-.2 1.1.4 2.3.6 3.6.6.6 0 1 .4 1 1V20c0 .6-.4 1-1 1A17 17 0 013 4c0-.6.4-1 1-1h3.5c.6 0 1 .4 1 1 0 1.3.2 2.5.6 3.6.1.3 0 .7-.2 1z"/></svg>
        555-014-2290</p>
      <p class="cover-info__web">www.olmorestaurant.com</p>
    </div>

    <ul class="cover-services">
      <li>Serving Breakfast Saturday &amp; Sunday</li>
      <li>Catering &amp; Private Party Hosting Available</li>
      <li>Friday Fish Fry · Saturday Prime Rib</li>
    </ul>
  </section>

</main>
</body>
</html>
```